Business Card for Industrial Distributor

We need a business card design for an industrial distributor. We sell machine parts for the manufacturing and oil industry. We would like the cards to look clean and modern but with a touch of industry.

Our colors are blue/white.

Please feel free to visit our website www.krovelmint.com

Target Market(s)

mexican manufacturers in the automobile/aerospace industry

Industry/Entity Type

Industrial

Colors
ffffff
0555a3

```html
<!DOCTYPE html>
<html lang="en">
<head>
<meta charset="utf-8">
<title>Krovelmint Business Card</title>
<link rel="stylesheet" href="https://fonts.googleapis.com/css2?family=Exo+2:wght@400;500;600;700&display=swap">
<style>
  :root {
    --page-bg: #e9e7e3;
    --card-white: #ffffff;
    --brand-blue: #27348b;
    --brand-mid: #0555a3;
    --brand-light: #1a6fbe;
    --text-grey: #777777;
    --text-dark: #6a6a6a;
    --rule-grey: #555555;
  }
  * { margin: 0; padding: 0; box-sizing: border-box; }
  html, body { width: 1200px; height: 987px; overflow: hidden; }
  body {
    background: var(--page-bg);
    font-family: "Exo 2", sans-serif;
    position: relative;
  }
  .card {
    position: absolute;
    left: 293px;
    width: 615px;
    height: 352px;
    border-radius: 19px;
    overflow: hidden;
  }
  .card-front { top: 130px; background: var(--card-white); }
  .card-back {
    top: 505px;
    background: radial-gradient(ellipse at 50% 45%, var(--brand-light) 0%, var(--brand-mid) 40%, var(--brand-blue) 100%);
  }
  .brand-name {
    position: absolute;
    left: 39px;
    top: 150px;
    width: 262px;
    font-weight: 700;
    font-size: 40px;
    line-height: 50px;
    color: var(--brand-blue);
    letter-spacing: -0.5px;
  }
  .divider {
    position: absolute;
    left: 327px;
    top: 60px;
    width: 1px;
    height: 224px;
    background: var(--rule-grey);
  }
  .divider-accent {
    position: absolute;
    left: 324px;
    top: 60px;
    width: 7px;
    height: 45px;
    background: linear-gradient(180deg, var(--brand-light), var(--brand-blue));
  }
  .details {
    position: absolute;
    left: 358px;
    top: 58px;
    color: var(--text-grey);
  }
  .person-name { font-size: 23px; font-weight: 600; line-height: 26px; color: var(--text-dark); }
  .person-title { font-size: 16px; font-weight: 600; line-height: 20px; color: var(--text-dark); }
  .company-name { margin-top: 12px; font-size: 16px; font-weight: 600; line-height: 22px; color: var(--text-dark); }
  .address { font-size: 16px; line-height: 22px; }
  .contact-list { list-style: none; margin-top: 10px; }
  .contact-list li {
    display: flex;
    align-items: center;
    font-size: 16px;
    line-height: 24px;
  }
  .contact-list svg { width: 15px; height: 15px; margin-right: 11px; fill: var(--text-grey); }
  .back-brand {
    position: absolute;
    left: 0;
    right: 0;
    top: 120px;
    text-align: center;
    font-weight: 700;
    font-size: 58px;
    line-height: 70px;
    color: var(--card-white);
  }
  .back-url {
    position: absolute;
    left: 0;
    right: 0;
    top: 300px;
    text-align: center;
    font-size: 17px;
    letter-spacing: 4.5px;
    color: var(--card-white);
  }
</style>
</head>
<body>
  <section class="card card-front">
    <div class="brand-name">Krovelmint</div>
    <div class="divider"></div>
    <div class="divider-accent"></div>
    <div class="details">
      <div class="person-name">DANIEL REYES</div>
      <div class="person-title">CEO/FOUNDER</div>
      <div class="company-name">Krovelmint International Corp.</div>
      <div class="address">4820 Harbor Line Rd.</div>
      <div class="address">Laredo.TX 78041</div>
      <ul class="contact-list">
        <li><svg viewBox="0 0 16 16" aria-hidden="true"><path d="M3.5 1l2.5 3-1.5 1.8c.9 2 2.6 3.7 4.6 4.6L11 8.9l3 2.5-1.3 2.8C7 14 2 9 1.6 3.2z"/></svg>(555) 310 - 4472</li>
        <li><svg viewBox="0 0 16 16" aria-hidden="true"><path d="M4 1h6l2 2v3H4z M1 7h14v6H1z M4 12h8v3H4z" /></svg>(555) 310 - 4480</li>
        <li><svg viewBox="0 0 16 16" aria-hidden="true"><path d="M1 3h14v10H1z M2 4l6 5 6-5" fill="none" stroke="#777" stroke-width="1.4"/></svg>sales@krovelmint.com</li>
        <li><svg viewBox="0 0 16 16" aria-hidden="true"><circle cx="8" cy="8" r="6.8"/><path d="M5 4c2 1 1 3 3 3s1 3 3 3M9 2c0 2 2 2 3 3" fill="none" stroke="#fff" stroke-width="1.2"/></svg>www.krovelmint.com</li>
      </ul>
    </div>
  </section>

  <section class="card card-back">
    <div class="back-brand">Krovelmint</div>
    <div class="back-url">WWW.KROVELMINT.COM</div>
  </section>
</body>
</html>
```